Tarjetas de visita para empresa de aluminio

Empresa con mas de 40 años vendiendo perfiles de aluminio.
Somos fábrica y almacén, queremos renovar la tarjeta de presentación de nuestros comerciales dando una imgen innovadora y tecnógica mezclado con la calidez del respeto al medio ambiente.
Añado el logo de la empresa y actual cara trasera de la tarjeta de visita, el logo es el simbolo ML y la marca TORVENIK EXTRUSION, la frase 2extrusion y lacado de aluminio" debe cambiarse por "Diseño, extrusión, lacado, anodizado y mecanizado de precisión de aluminio" o en su defecto incluir todos esos servicios que hacemos o una frase mas pegadiza.

We are an aluminium factory, we produce and stock profiles of aluminium.
we want to renew visit card of our sellers, we are looking for something that show innovation, tecnology and environment respect.
Upload our actual logo and back of visit card, logo ML and brand TORVENIK EXTRUSION must be keept.
Text "Extrusion y lacado de aluminio" must be changed for "Diseño, extrusion, lacado, anodizado y mecanizado de precisión de aluminio" or something like that

```html
<!DOCTYPE html>
<html lang="es">
<head>
<meta charset="utf-8">
<title>Tarjetas de visita – Aluminios Norvalis</title>
<link href="https://fonts.googleapis.com/css2?family=Arimo:wght@400;700&display=swap" rel="stylesheet">
<style>
  :root{
    --stage:#3b3b3d;
    --card:#121214;
    --blue:#4a9ee0;
    --text:#e6e6e6;
    --silver:#cfd2d6;
  }
  *{box-sizing:border-box;margin:0;padding:0}
  html,body{width:1200px;height:801px;overflow:hidden;background:var(--stage);font-family:"Arimo",Arial,sans-serif}
  .stage{position:relative;width:1200px;height:801px}
  .card{position:absolute;top:240px;width:540px;height:310px;background:var(--card);border-bottom:3px solid var(--blue);border-left:2px solid var(--blue);box-shadow:0 10px 30px rgba(0,0,0,.45)}
  .card--front{left:45px}
  .card--back{left:615px}

  .front__brand{position:absolute;left:0;top:0;width:250px;height:100%;display:flex;align-items:center;justify-content:center}
  .brand-name{color:var(--blue);font-size:18px;font-weight:700;letter-spacing:1px;white-space:nowrap}

  .front__divider{position:absolute;left:250px;top:28px;width:2px;height:254px;background:var(--blue)}

  .front__info{position:absolute;left:276px;top:34px;right:16px;color:var(--text);font-size:13.5px;line-height:1.35}
  .person__name{color:var(--blue);font-weight:700;font-size:17px}
  .person__role{margin-bottom:10px}
  .address{margin-bottom:12px}
  .contact{list-style:none}
  .contact li{display:flex;align-items:center;gap:8px}
  .contact svg{width:12px;height:12px;flex:none;fill:var(--text)}

  .back__brand{position:absolute;left:0;right:0;top:110px;text-align:center;color:var(--silver);font-size:26px;font-weight:700;letter-spacing:2px}
  .back__tagline{position:absolute;left:0;right:0;bottom:40px;text-align:center;color:var(--text);font-size:15px}
</style>
</head>
<body>
<main class="stage">
  <section class="card card--front">
    <div class="front__brand">
      <p class="brand-name">ALUMINIOS NORVALIS</p>
    </div>
    <div class="front__divider"></div>
    <div class="front__info">
      <p class="person__name">MARCOS LEDESMA RUIZ</p>
      <p class="person__role">Comercial</p>
      <p class="address">Pol. Ind. Los Olivos-C/4 Nº 22<br>41890 SANTA ALBERA (Sevilla)<br>Apartado de Correos 254</p>
      <ul class="contact">
        <li><svg viewBox="0 0 12 12"><rect x="3" y="0" width="6" height="12" rx="1"/></svg>600 12 34 56</li>
        <li><svg viewBox="0 0 12 12"><path d="M2 1h3l1 3-2 1a7 7 0 0 0 3 3l1-2 3 1v3c-6 0-10-4-10-9z"/></svg>955 00 11 22</li>
        <li><svg viewBox="0 0 12 12"><rect x="1" y="4" width="10" height="6" rx="1"/><rect x="3" y="1" width="6" height="3"/></svg>955 00 11 33</li>
        <li><svg viewBox="0 0 12 12"><path d="M0 2h12v8H0z M0 2l6 5 6-5"/></svg>marcosledesma@torvenik.com</li>
        <li><svg viewBox="0 0 12 12"><circle cx="6" cy="6" r="6"/></svg>www.torvenik.com</li>
      </ul>
    </div>
  </section>

  <section class="card card--back">
    <p class="back__brand">TORVENIK EXTRUSION</p>
    <p class="back__tagline">Diseño, extrusion, lacado, anodizado y mecanizado de precisión de aluminio</p>
  </section>
</main>
</body>
</html>
```